Coastal waterside shopping complex needs a billboard sign

"Harbor Quay" is the name of a building which comprises 4 shops in a coastal waterside location. We need a 2440mm (Wide) x 1100mm (High) "Harbor Quay" billboard design that will fit with the coastal theme but is modern and contemporary, positioning the building as a high class mini shopping complex.

The photo below is for reference only. We only need a design for the "Harbor Quay" sign.

The end product will need to be an EPS scalable vector file.

Industry/Entity Type

Shopping

```html
<!DOCTYPE html>
<html lang="en">
<head>
<meta charset="utf-8">
<title>Harbor Quay Billboard</title>
<link rel="stylesheet" href="https://fonts.googleapis.com/css2?family=Poppins:wght@300;700;800&display=swap">
<style>
  :root {
    --ink: #000000;
    --paper: #ffffff;
    --aqua: #00f2ee;
    --ocean: #1a9ad9;
    --sand: #dcdedd;
    --sea-deep: #1b7fa0;
    --canvas: #f2f2f2;
  }
  html, body {
    margin: 0;
    padding: 0;
    width: 1200px;
    height: 1200px;
    overflow: hidden;
    background: var(--canvas);
  }
  .billboard {
    position: absolute;
    left: 50px;
    top: 352px;
    width: 1100px;
    height: 497px;
    display: block;
    box-shadow: 0 8px 22px rgba(0,0,0,0.25);
  }
  .title {
    font-family: "Poppins", sans-serif;
    font-weight: 800;
    font-size: 174px;
    letter-spacing: -4px;
  }
  .title-first { fill: var(--paper); }
  .title-second { fill: var(--aqua); }
  .tagline {
    font-family: "Poppins", sans-serif;
    font-weight: 300;
    font-size: 27px;
    fill: var(--paper);
  }
  .badge-number {
    font-family: "Poppins", sans-serif;
    font-weight: 700;
    font-size: 25px;
    fill: var(--paper);
  }
</style>
</head>
<body>
<svg class="billboard" viewBox="0 0 1050 474" xmlns="http://www.w3.org/2000/svg">
  <defs>
    <linearGradient id="coast-tones" x1="0" y1="0" x2="0" y2="1">
      <stop offset="0" stop-color="#6fa860"/>
      <stop offset="0.16" stop-color="#d8dad8"/>
      <stop offset="0.45" stop-color="var(--sand)"/>
      <stop offset="0.62" stop-color="#eef3f5"/>
      <stop offset="0.75" stop-color="#4fb4cb"/>
      <stop offset="1" stop-color="var(--sea-deep)"/>
    </linearGradient>
  </defs>

  <g class="coast-photo" role="img" aria-label="Aerial view of a tropical beach with palm trees, white sand and turquoise surf">
    <rect x="0" y="0" width="1050" height="474" fill="url(#coast-tones)"/>
  </g>

  <path class="wave-band-aqua" d="M0 0 H815 Q868 265 640 474 H0 Z" fill="var(--aqua)"/>
  <path class="wave-band-ocean" d="M0 0 H792 Q842 258 612 474 H0 Z" fill="var(--ocean)"/>
  <path class="panel" d="M0 0 H750 Q800 250 574 474 H0 Z" fill="var(--ink)"/>

  <text class="title title-first" x="68" y="199">Harbor</text>
  <text class="title title-second" x="68" y="365">Quay</text>
  <text class="tagline" x="74" y="412">mini shopping complex</text>

  <g class="number-badge">
    <circle cx="1062" cy="488" r="150" fill="var(--ocean)"/>
    <circle cx="1062" cy="488" r="142" fill="var(--aqua)"/>
    <circle cx="1062" cy="488" r="134" fill="var(--ink)"/>
    <text class="badge-number" x="963" y="450">No.01</text>
  </g>
</svg>
</body>
</html>
```